Embers Business Card x 4 and Coaster x 1

Hi We need a business card design for an existing company.

All we need is for someone to EXACTLY copy the attached files... and give them back to us in HIGH RES.

They need to be re-made in photoshop or similar and sent back...

The dimensions can be larger than actual size - but they need to be scale.

BUSINESS CARDS X 4 - DOUBLE SIDED standard business card size
FILE 2 & 3 Back and Front of generic card
FILE 4 - Front of all 3 personalised business cards
FILe 5, 6 ,7 - Back of each personalised business cards

COASTER X 1 - SINGLE SIDED DIMENSIONS (9CM x 9CM ) ( FILE 1)

ALSO Attached is the original photo for the wine bottle collage. FILE 8 HIGH RES

PLEASE NOTE : FONT IS MONOTON

Target Market(s)

N/A

Industry/Entity Type

Business

Contact Information for Business Card

AS PER FILES ATTACHED 1xGENERIC ( NO NAME ) 3X PERSONALISED 1X COASTER

Font styles to use
Other font styles liked:
• MONOTON

Requirements
Must have
• JUST NEED PROVIDED FILES COPIED PLEASE - AS CLOSE AS POSSIBLE

```html
<!DOCTYPE html>
<html lang="en">
<head>
<meta charset="utf-8">
<title>Embers Business Cards and Coaster</title>
<link href="https://fonts.googleapis.com/css2?family=Open+Sans:wght@400;700;800&display=swap" rel="stylesheet">
<style>
  :root {
    --page: #ffffff;
    --card: #262626;
    --logo: #a3a3a3;
    --ink: #f2f2f2;
    --muted: #c9c9c9;
    --coaster-mark: #3a3a3a;
  }
  html, body { margin: 0; padding: 0; overflow: hidden; }
  body { width: 859px; height: 1200px; background: var(--page); position: relative; font-family: "Open Sans", Arial, sans-serif; }
  .card {
    position: absolute; width: 270px; height: 370px; background: var(--card);
    box-shadow: 0 2px 6px rgba(0,0,0,.35); overflow: hidden; color: var(--ink);
  }
  .brand {
    position: absolute; top: 14px; left: 0; right: 0; text-align: center;
    font-family: "Open Sans", Arial, sans-serif; font-weight: 800;
    font-size: 38px; line-height: 1; color: var(--logo); letter-spacing: 1px;
  }
  .address { position: absolute; top: 58px; left: 0; right: 0; text-align: center; font-size: 7px; font-weight: 700; color: var(--muted); }
  .person { position: absolute; top: 150px; left: 0; right: 0; text-align: center; }
  .person .name { font-size: 14px; font-weight: 700; letter-spacing: .5px; margin-bottom: 6px; }
  .person .line { font-size: 8px; line-height: 11px; color: var(--muted); }
  .web { position: absolute; bottom: 30px; left: 0; right: 0; text-align: center; font-size: 8px; color: var(--muted); }
  .domain {
    position: absolute; bottom: 48px; left: 0; right: 0; text-align: center;
    font-family: "Open Sans", Arial, sans-serif; font-weight: 800;
    font-size: 30px; line-height: 1; color: var(--logo); letter-spacing: 1px;
  }
  .photo { position: absolute; inset: 0; }
  .photo-card .brand { color: var(--ink); z-index: 2; }
  .photo-card .address { z-index: 2; }
  .coaster { width: 312px; height: 318px; }
  .coaster .wordmark {
    position: absolute; right: 16px; bottom: 14px; line-height: 1;
    font-family: "Open Sans", Arial, sans-serif; font-weight: 800;
    font-size: 30px; color: var(--coaster-mark); letter-spacing: 1px;
  }
</style>
</head>
<body>
  <section class="card" style="left:14px; top:14px;">
    <div class="brand">EMBERS</div>
    <div class="address">12 Lantern Lane Central Hong Kong</div>
    <div class="person">
      <div class="name">TED MARLOW</div>
      <div class="line">(+852) 6100 2200</div>
      <div class="line">(+852) 6100 3300</div>
      <div class="line">ted@embers.hk</div>
    </div>
    <div class="web">www.embers.hk</div>
  </section>

  <section class="card" style="left:294px; top:14px;">
    <div class="brand">EMBERS</div>
    <div class="address">12 Lantern Lane Central Hong Kong</div>
    <div class="person">
      <div class="name">JONAH MARLOW</div>
      <div class="line">(+852) 6100 4400</div>
      <div class="line">jonah@embers.hk</div>
    </div>
    <div class="web">www.embers.hk</div>
  </section>

  <section class="card" style="left:574px; top:14px;">
    <div class="brand">EMBERS</div>
    <div class="address">12 Lantern Lane Central Hong Kong</div>
    <div class="person">
      <div class="name">MILO TAN</div>
      <div class="line">(+852) 6100 5500</div>
      <div class="line">milo@embers.hk</div>
    </div>
    <div class="web">www.embers.hk</div>
  </section>

  <section class="card" style="left:14px; top:456px;">
    <div class="brand">EMBERS</div>
    <div class="address">12 Lantern Lane Central Hong Kong</div>
    <div class="domain">EMBERS.HK</div>
  </section>

  <section class="card photo-card" style="left:294px; top:456px;">
    <div class="photo" role="img" aria-label="Wine bottle collage on folded white paper strips"
         style="background: linear-gradient(180deg, #262626 0%, #262626 20%, rgba(38,38,38,0) 34%), radial-gradient(ellipse at 45% 58%, #5e3f36 0%, #3a2e2a 25%, #d9d6d0 48%, #8d8a85 72%, #2c2c2c 100%);"></div>
    <div class="brand">EMBERS</div>
    <div class="address">12 Lantern Lane Central Hong Kong</div>
  </section>

  <section class="card photo-card" style="left:574px; top:456px;">
    <div class="photo" role="img" aria-label="Wine bottle collage tinted with red, blue and yellow bands"
         style="background: linear-gradient(180deg, #262626 0%, #262626 18%, #d98a80 24%, #c77b73 44%, #6d6fc0 48%, #5c5fb0 66%, #d8c85a 70%, #c9b94a 90%, #262626 96%);"></div>
    <div class="brand">EMBERS</div>
    <div class="address">12 Lantern Lane Central Hong Kong</div>
  </section>

  <section class="card coaster" style="left:274px; top:866px;">
    <div class="photo" role="img" aria-label="Wine bottle collage on folded white paper strips"
         style="background: radial-gradient(ellipse at 40% 40%, #5a3f36 0%, #3a2e2a 22%, #e2dfda 45%, #a9a59f 70%, #f0efec 100%);"></div>
    <div class="wordmark">EMBERS</div>
  </section>
</body>
</html>
```